Marrowfield tri-fold DL Flyer Clinic

Marrowfield is an award-winning organisation providing dynamic and creative ways for children, young people, adults and families to make positive change and achieve fulfilling lives. We have a general psychology clinic and also offer KVMB services for people with high and intensive needs.  We have recently opened our purpose fitted clinic and are now looking to create a flyer to use in our promotions of the clinic.
We are after an a4 colour double sided flyer in a tri fold to DL format.   We are looking for a design that is simple and dynamic whilst keeping in line with our branding.  I envisage this brochure could use some photos of the space (in a dynamic way) and potentially some illustration.  I have attached a number of files to provide further background and also images of the space that could be used.   I have also attached the draft text for the flyer and current map we use to send to clients.
The winning design will need to be hi-res and ready for print.

- Poppins

```html
<!DOCTYPE html>
<html lang="en">
<head>
<meta charset="utf-8">
<title>Marrowfield tri-fold DL flyer</title>
<link href="https://fonts.googleapis.com/css2?family=Poppins:wght@400;500;600;700&display=swap" rel="stylesheet">
<style>
:root{
  --bg:#e6e6e6;
  --paper:#ffffff;
  --green:#6f8f79;
  --green-text:#6b9a70;
  --teal:#7f9ea0;
  --peach:#c9a48c;
  --ink:#2e2e2e;
  --body:#4a4a4a;
  --stripe:#ececec;
  --photo-a:#9aa0a3;
  --photo-b:#5e6468;
}
*{box-sizing:border-box;margin:0;padding:0}
html,body{width:1200px;height:3253px;overflow:hidden}
body{background:var(--bg);font-family:'Poppins',sans-serif;color:var(--body);position:relative}
.sheet{position:absolute;left:40px;width:1120px;height:865px;background:var(--paper);display:grid;grid-template-columns:373px 374px 373px;box-shadow:0 4px 18px rgba(0,0,0,.12)}
.sheet--outside{top:700px}
.sheet--inside{top:1685px}
.panel{position:relative;height:865px;overflow:hidden}
.panel--green{background:var(--green);color:#fff}
.abs{position:absolute}
.photo{background:linear-gradient(160deg,var(--photo-a),var(--photo-b))}
.photo--colour{background:linear-gradient(180deg,#7fb0d8 0%,#a9c4d6 45%,#8a6a58 70%,#6e7a60 100%)}
.photo--warm{background:linear-gradient(160deg,#c9c9c9,#6b6b6b)}

/* about panel */
.tab{position:absolute;left:0;top:38px;width:262px;height:32px;background:var(--teal);color:#fff;font-weight:700;font-size:17px;line-height:32px;padding-left:40px;border-radius:0 8px 8px 0;letter-spacing:.3px}
.about-copy{position:absolute;left:36px;top:104px;width:315px;font-size:11.4px;line-height:14px;color:var(--body)}
.about-copy p+p{margin-top:14px}
.entrance-frame{left:34px;top:455px;width:314px;height:242px;border:1px solid #ddd;box-shadow:0 1px 6px rgba(0,0,0,.15);padding:8px;background:#fff}
.entrance-frame .photo--colour{width:100%;height:100%}
.callout{position:absolute;background:var(--peach);color:#fff;text-align:center;border-radius:3px}
.callout--entrance{left:216px;top:391px;width:133px;height:54px;padding:3px 4px}
.callout--entrance strong{display:block;font-size:10.5px;font-weight:600}
.callout--entrance span{display:block;font-size:7px;line-height:8.5px}
.label{position:absolute;left:218px;width:131px;height:15px;font-size:10px;line-height:15px;color:#fff;text-align:center;border-radius:3px}
.label--cafe{top:703px;background:var(--teal)}
.label--access{top:724px;background:var(--green)}
.url-bar{position:absolute;top:804px;height:23px;font-size:14px;font-weight:600;letter-spacing:5px;color:#fff;text-align:center;line-height:23px;border-radius:2px}
.url-bar--green{left:63px;width:262px;background:var(--green)}
.url-bar--peach{left:48px;width:277px;background:var(--peach)}

/* contact panel */
.map{left:19px;top:38px;width:335px;height:363px;background:linear-gradient(135deg,#f4f4f2,#dfe6dc);border:4px solid #fff}
.pill{position:absolute;left:50%;transform:translateX(-50%);height:36px;border-radius:10px;color:#fff;font-weight:700;text-align:center}
.pill--contact{top:468px;width:216px;background:var(--teal);border:2px solid #e3ecec;font-size:22px;line-height:32px;letter-spacing:.5px}
.icon{position:absolute;left:50%;transform:translateX(-50%);width:34px;height:34px;border-radius:50%;background:#fff;display:flex;align-items:center;justify-content:center}
.icon svg{width:18px;height:18px}
.contact-line{position:absolute;left:0;width:100%;text-align:center;color:#fff}
.contact-phone{top:559px;font-size:21px;font-weight:500}
.contact-web{top:656px;font-size:14px}
.contact-mail{top:723px;font-size:14px}
.contact-address{top:796px;font-size:13.5px;line-height:18px}

/* cover panel */
.brand{position:absolute;left:0;width:100%;text-align:center}
.brand__name{top:46px;font-size:38px;font-weight:500;color:#3d3d3d;letter-spacing:.3px}
.brand__mark{display:inline-block;width:22px;height:22px;background:var(--green);border-radius:50%;margin-right:10px;vertical-align:middle}
.brand__tag{top:98px;font-size:9px;letter-spacing:1px;color:#555}
.cover-photo{left:0;top:126px;width:373px;height:470px}
.cover-shapes{position:absolute;left:0;top:126px}
.headline{position:absolute;left:0;width:100%;text-align:center;line-height:1}
.headline--a{top:626px;font-size:26px;font-weight:700;color:var(--ink)}
.headline--b{top:653px;font-size:26px;font-weight:700;color:var(--green-text)}
.headline--c{top:681px;font-size:21px;font-weight:500;color:var(--ink)}
.cover-copy{position:absolute;left:22px;top:712px;width:329px;text-align:center;font-size:10.8px;line-height:13px;color:var(--body)}

/* services */
.services-title{position:absolute;left:40px;top:26px;font-size:25px;font-weight:700;color:var(--ink);z-index:2}
.services-title span{color:var(--green-text)}
.services-rule{position:absolute;left:40px;top:70px;width:1040px;height:2px;background:var(--teal);z-index:2}
.services-rule::after{content:"";position:absolute;right:-4px;top:-3px;width:8px;height:8px;border-radius:50%;background:var(--teal)}
.pill--list{top:84px;width:313px;height:52px;font-size:13.5px;font-weight:500;line-height:17px;padding-top:9px;border-radius:12px}
.pill--teal{background:var(--teal)}
.pill--peach{background:var(--peach);height:46px;line-height:46px;padding-top:0;width:283px}
.list{position:absolute;left:30px;width:313px;list-style:none}
.list li{position:relative;padding-left:24px;font-size:10.6px;font-weight:500;color:#333}
.list li::before{content:"";position:absolute;left:11px;top:50%;width:5px;height:5px;margin-top:-3px;border:1.5px solid var(--green);border-radius:50%}
.list--concerns{top:164px}
.list--concerns li{height:24px;line-height:24px}
.list--concerns li:nth-child(even){background:var(--stripe)}
.list--approaches{top:164px;left:24px;width:323px}
.list--approaches li{color:#fff;line-height:27px;min-height:27px}
.list--approaches li::before{border-color:#fff}
.list--approaches li:nth-child(even){background:#fff;color:#333;line-height:18px;min-height:18px;margin:4px 0}
.list--approaches li:nth-child(even)::before{border-color:var(--green)}
.list--approaches li.wrap{line-height:22px}
.list--assessments{top:164px}
.list--assessments li{height:27px;line-height:27px}
.list--assessments li:nth-child(even){background:var(--stripe)}
.note{position:absolute;left:24px;top:424px;width:313px;height:77px;background:var(--peach);color:#fff;border-radius:10px;padding:10px 16px;font-size:10.6px;line-height:13px}
.photo-frame{position:absolute;left:24px;top:569px;width:323px;height:267px;border:5px solid #fff}
.photo-frame--green{border-color:var(--green)}
.photo-frame div{width:100%;height:100%}
</style>
</head>
<body>

<section class="sheet sheet--outside">
  <!-- About panel -->
  <div class="panel">
    <div class="tab">ABOUT MARROWFIELD</div>
    <div class="about-copy">
      <p>Marrowfield is an award-winning organisation and a Certified Social Enterprise, providing dynamic and creative ways for children, young people, adults and families to make positive change and achieve fulfilling lives. In our new purpose fitted clinic, we provide a safe space for confidential psychology, counselling, and support services. We also offer KVMB services for people with high and intensive needs.</p>
      <p>Our team has extensive experience working with mental health issues and complex disability and people who are neurodivergent to live their best lives. We provide quality, evidence-informed services to adults and children with complex needs along with their families and networks.</p>
    </div>
    <div class="callout callout--entrance">
      <strong>Marrowfield Entrance</strong>
      <span>Up the stairs and to the right, accessible entrance via Tannery Lane Cafe</span>
    </div>
    <svg class="abs" style="left:0;top:0" width="373" height="865" aria-hidden="true">
      <polyline points="216,418 166,418 166,712 218,712" fill="none" stroke="#3f5f49" stroke-width="1.5"/>
      <polyline points="74,640 74,731 218,731" fill="none" stroke="#3f5f49" stroke-width="1.5"/>
      <polygon points="74,632 69,642 79,642" fill="#3f5f49"/>
    </svg>
    <div class="abs entrance-frame"><div class="photo--colour" role="img" aria-label="Photo of the clinic building exterior with glass entrance under a blue sky"></div></div>
    <svg class="abs" style="left:0;top:0" width="373" height="865" aria-hidden="true">
      <line x1="166" y1="500" x2="166" y2="712" stroke="#3f5f49" stroke-width="1.5"/>
      <line x1="74" y1="640" x2="74" y2="731" stroke="#3f5f49" stroke-width="1.5"/>
      <polygon points="74,632 69,642 79,642" fill="#3f5f49"/>
    </svg>
    <div class="label label--cafe">Tannery Lane Cafe</div>
    <div class="label label--access">Accessible Entrance</div>
    <div class="url-bar url-bar--green">www.Marrowfield.au</div>
  </div>

  <!-- Contact panel -->
  <div class="panel panel--green">
    <div class="abs map" role="img" aria-label="Street map showing the clinic location, nearby tram stops and parking"></div>
    <div class="pill pill--contact">CONTACT US</div>
    <div class="icon" style="top:501px"><svg viewBox="0 0 24 24"><path d="M6.6 10.8a15.1 15.1 0 0 0 6.6 6.6l2.2-2.2a1 1 0 0 1 1-.25 11.4 11.4 0 0 0 3.6.57 1 1 0 0 1 1 1V20a1 1 0 0 1-1 1A17 17 0 0 1 3 4a1 1 0 0 1 1-1h3.5a1 1 0 0 1 1 1c0 1.25.2 2.45.57 3.57a1 1 0 0 1-.25 1z" fill="#6f8f79"/></svg></div>
    <div class="contact-line contact-phone">03 5550 1842</div>
    <div class="icon" style="top:602px"><svg viewBox="0 0 24 24" fill="none" stroke="#6f8f79" stroke-width="1.8"><circle cx="12" cy="12" r="9"/><ellipse cx="12" cy="12" rx="4" ry="9"/><line x1="3" y1="12" x2="21" y2="12"/></svg></div>
    <div class="contact-line contact-web">www.Marrowfield.au</div>
    <div class="icon" style="top:677px"><svg viewBox="0 0 24 24" fill="none" stroke="#6f8f79" stroke-width="1.8"><rect x="3" y="6" width="18" height="12" rx="1"/><polyline points="3,6 12,13 21,6"/></svg></div>
    <div class="contact-line contact-mail">clinic@marrowfield.au</div>
    <div class="icon" style="top:751px"><svg viewBox="0 0 24 24"><path d="M12 2a7 7 0 0 0-7 7c0 5 7 13 7 13s7-8 7-13a7 7 0 0 0-7-7zm0 9.5A2.5 2.5 0 1 1 12 6.5a2.5 2.5 0 0 1 0 5z" fill="#6f8f79"/></svg></div>
    <div class="contact-line contact-address">Harbourmasters Building,<br>42 Kellbrook Rd, Ashgrove VIC 3999</div>
  </div>

  <!-- Cover panel -->
  <div class="panel">
    <div class="brand brand__name"><span class="brand__mark"></span>Marrowfield</div>
    <div class="brand brand__tag">SUPPORT • THERAPY • LEARNING</div>
    <div class="abs cover-photo photo" role="img" aria-label="Black and white photo of children lying in a circle making binocular shapes with their hands"></div>
    <svg class="cover-shapes" width="373" height="500" aria-hidden="true">
      <polygon points="373,260 210,360 373,400" fill="#c9a48c"/>
      <polygon points="0,330 373,420 373,500 0,500" fill="#6f8f79"/>
      <polygon points="0,480 186,430 373,480 373,500 0,500" fill="#ffffff"/>
    </svg>
    <div class="headline headline--a">POSITIVE BEHAVIOUR</div>
    <div class="headline headline--b">SUPPORT SERVICES</div>
    <div class="headline headline--c">FOR ADULTS &amp; CHILDREN</div>
    <div class="cover-copy">Marrowfield is an award-winning organisation providing dynamic and creative ways for children, young people, adults and families to make positive change and achieve fulfilling lives</div>
    <div class="url-bar url-bar--peach">www.Marrowfield.au</div>
  </div>
</section>

<section class="sheet sheet--inside">
  <div class="services-title">OUR <span>SERVICES</span></div>
  <div class="services-rule"></div>

  <div class="panel">
    <div class="pill pill--list pill--teal">We can support children,<br>adolescents and adults experiencing</div>
    <ul class="list list--concerns">
      <li>Anxiety</li><li>Panic Attacks</li><li>Phobias</li><li>Depression</li><li>Complex trauma</li>
      <li>Post-Traumatic Stress Disorder (PTSD)</li><li>Autism Spectrum Disorder (ASD)</li><li>Learning Disorders</li>
      <li>Intellectual Disability</li><li>Dual Disability</li><li>Attention Deficit Hyperactivity Disorder (ADHD)</li>
      <li>Bipolar Disorder</li><li>Schizophrenia</li><li>Obsessive-Compulsive Disorder</li><li>Personality Disorders</li>
      <li>Challenging Behaviours</li><li>Relationship Issues</li><li>LGBTQIA+ and Sexuality Issues</li>
      <li>Drug and Alcohol Issues</li><li>Addictions</li><li>Grief and Loss</li><li>Home/School/Workplace Stress</li>
      <li>Bullying</li><li>Body Image and Self Esteem</li><li>Life Transitions</li><li>Chronic Illness</li>
    </ul>
  </div>

  <div class="panel panel--green">
    <div class="pill pill--list pill--peach">Therapeutic Approaches</div>
    <ul class="list list--approaches">
      <li>Cognitive Behavioural Therapy (CBT)</li>
      <li>Acceptance and Commitment Therapy (ACT)</li>
      <li>Dialectical Behavioural Therapy (DBT)</li>
      <li>Mindfulness Based Therapies</li>
      <li>Compassion Focussed Therapies</li>
      <li class="wrap">Eye Movement Desensitisation and<br>Reprocessing (EMDR)</li>
      <li>Schema Therapy</li>
      <li>Internal Family Systems Therapy</li>
      <li>Motivational Interviewing</li>
      <li>Narrative Therapy</li>
      <li>Art Therapy and Expressive Therapies</li>
      <li>Play Therapy</li>
    </ul>
    <div class="photo-frame"><div class="photo--warm" role="img" aria-label="Black and white photo of a smiling group of teenagers standing arm in arm"></div></div>
  </div>

  <div class="panel">
    <div class="pill pill--list pill--teal">Psychological Assessments for<br>Children, Adolescents and Adults</div>
    <ul class="list list--assessments">
      <li>Cognitive Assessments (IQ Testing)</li><li>Autism Assessments (ADOS-2)</li>
      <li>Specific Learning Disorder Assessments</li><li>Intellectual Disability Assessments</li>
      <li>Memory Assessments</li><li>Personality Assessments</li><li>Vocational Assessments</li>
      <li>Mood Assessments</li><li>Behavioural Assessments</li>
    </ul>
    <div class="note">Marrowfield can accept referrals for psychological services under Healthcover, KVMB, RSA, Workshield, EAP, and client self-referrals (private health insurance rebates may apply).</div>
    <div class="photo-frame photo-frame--green"><div class="photo--warm" role="img" aria-label="Black and white photo of children raising their arms outdoors"></div></div>
  </div>
</section>

</body>
</html>
```